Desing for real estate offers- Package system

The word should be graphically clear and understandable. There are 3 packages that the customer can buy: the basic package is red, the medicinal package is green and the carefree package is blue. See the Word document in the appendix. End file should be a Word, as we need to chance the text. It should also match the website as well as the business card.
https://brelvona.domistra.ch/
Colors:
Green 1: R: 187, G: 214, B: 49
Green 2: R: 119, G: 187, W: 66

Target Market(s)

Real estate company

Font styles to use
Serif
Sans Serif

```html
<!DOCTYPE html>
<html lang="de">
<head>
<meta charset="utf-8">
<title>Brelvona – Verkaufspakete</title>
<link href="https://fonts.googleapis.com/css2?family=Archivo+Black&family=Barlow:ital,wght@0,500;0,600;1,500;1,600&display=swap" rel="stylesheet">
<style>
  :root {
    --green-1: rgb(187, 214, 49);
    --green-2: rgb(119, 187, 66);
    --ink: #1c1c1c;
    --page: #ffffff;

    --basis-bg-light: #fbecec;
    --basis-bg: #f3d3d3;
    --basis-title: #e08a8a;
    --basis-accent: #c83a3a;

    --medium-bg-light: #eef5ea;
    --medium-bg: #d6e9cc;
    --medium-title: #9fcf86;
    --medium-accent: rgb(119, 187, 66);

    --sorglos-bg-light: #ebf2fa;
    --sorglos-bg: #d2e1f1;
    --sorglos-title: #86aedb;
    --sorglos-accent: #2f6db3;
  }
  * { box-sizing: border-box; margin: 0; padding: 0; }
  html, body { width: 1200px; height: 1129px; overflow: hidden; background: var(--page); }
  body { font-family: "Barlow", sans-serif; color: var(--ink); position: relative; }

  .brand {
    position: absolute; left: 48px; top: 68px;
    display: flex; align-items: center; gap: 10px;
    font-weight: 600; font-size: 40px; color: var(--green-2);
  }
  .brand-dot { width: 14px; height: 14px; border-radius: 50%; background: var(--green-2); }

  .contact {
    position: absolute; left: 780px; top: 36px;
    list-style: none; font-size: 17px; font-weight: 500; line-height: 1.55;
  }
  .contact li { display: flex; align-items: center; gap: 8px; }
  .contact svg { width: 16px; height: 16px; flex: none; }

  .prices {
    position: absolute; left: 300px; top: 168px; width: 860px;
    font-size: 17px; font-weight: 600; line-height: 1.3;
  }
  .prices p { margin-bottom: 10px; }

  .band-top { position: absolute; left: 300px; top: 282px; width: 860px; height: 46px; }
  .band-top .upper { position: absolute; left: 0; top: 0; width: 100%; height: 22px; background: linear-gradient(90deg, var(--green-1), var(--green-2)); }
  .band-top .lower { position: absolute; left: 0; top: 22px; width: 100%; height: 24px; background: linear-gradient(90deg, var(--green-2), var(--green-1)); opacity: .9; }

  .package {
    position: absolute; left: 300px; width: 860px; overflow: hidden;
    padding: 14px 40px 10px 34px;
    font-size: 17px; font-weight: 500; line-height: 24px;
    border-left: 6px solid var(--accent);
    background: linear-gradient(90deg, var(--bg-light), var(--bg));
  }
  .package-title {
    position: absolute; right: 14px; top: -2px;
    font-family: "Archivo Black", sans-serif; font-size: 46px; line-height: 1;
    color: var(--title); letter-spacing: 1px;
  }
  .package-lead { margin-bottom: 6px; }
  .package ul { padding-left: 56px; }
  .package li { padding-left: 6px; }
  .package li::marker { color: var(--accent); }

  .package--basis {
    --bg-light: var(--basis-bg-light); --bg: var(--basis-bg);
    --title: var(--basis-title); --accent: var(--basis-accent);
    top: 334px; height: 296px; padding-top: 22px;
  }
  .package--medium {
    --bg-light: var(--medium-bg-light); --bg: var(--medium-bg);
    --title: var(--medium-title); --accent: var(--medium-accent);
    top: 636px; height: 150px;
  }
  .package--sorglos {
    --bg-light: var(--sorglos-bg-light); --bg: var(--sorglos-bg);
    --title: var(--sorglos-title); --accent: var(--sorglos-accent);
    top: 792px; height: 246px;
  }

  .band-bottom { position: absolute; left: 40px; top: 1044px; width: 800px; height: 34px; }
  .band-bottom .upper { position: absolute; left: 0; top: 0; width: 100%; height: 16px; background: var(--green-1); }
  .band-bottom .lower { position: absolute; left: 0; top: 16px; width: 100%; height: 18px; background: linear-gradient(90deg, var(--green-1), var(--green-2)); }

  .note {
    position: absolute; left: 150px; top: 1084px; width: 900px;
    text-align: center; font-style: italic; font-weight: 600; font-size: 15px; line-height: 20px;
  }
</style>
</head>
<body>
  <div class="brand"><span class="brand-dot"></span>Brelvona</div>

  <ul class="contact">
    <li><svg viewBox="0 0 16 16"><circle cx="8" cy="8" r="8" fill="rgb(119,187,66)"/><path d="M5 4.5l1.6-.4.9 2-1 .8a5 5 0 0 0 2.6 2.6l.8-1 2 .9-.4 1.6c-3.4.2-6.7-3.1-6.5-6.5z" fill="#fff"/></svg>044 612 37 19</li>
    <li><svg viewBox="0 0 16 16"><circle cx="8" cy="8" r="8" fill="rgb(119,187,66)"/><rect x="4" y="5" width="8" height="6" rx="1" fill="#fff"/><path d="M4.5 5.5L8 8.3l3.5-2.8" stroke="rgb(119,187,66)" fill="none"/></svg>lena.furrer@brelvona.ch</li>
    <li><svg viewBox="0 0 16 16"><circle cx="8" cy="8" r="8" fill="rgb(119,187,66)"/><circle cx="8" cy="8" r="4.5" fill="none" stroke="#fff"/><path d="M3.5 8h9M8 3.5c-2 2.5-2 6.5 0 9M8 3.5c2 2.5 2 6.5 0 9" stroke="#fff" fill="none" stroke-width=".8"/></svg>brelvona.ch</li>
  </ul>

  <div class="prices">
    <p>Basis-Paket 8'500.- CHF exkl. MWST</p>
    <p>Medium-Paket 10'900 CHF exkl. MWST</p>
    <p>Sorglos: 2% vom Verkaufspreis inkl. MWST (von Grundstückgewinnsteuer abziehbar)</p>
  </div>

  <div class="band-top"><div class="upper"></div><div class="lower"></div></div>

  <section class="package package--basis">
    <h2 class="package-title">BASIS</h2>
    <ul>
      <li>Begehung Verkaufsobjekt</li>
      <li>Hedonische Schätzung intern &amp; Bank</li>
      <li>Marketing &amp; Vertriebskonzept</li>
      <li>Unterlagen einfordern- STWEG Protokolle, GB Auszug u.s.w wenn nötig</li>
      <li>Fotografieren &amp; Ausmessen der Immobilie</li>
      <li>Grundriss zeichnen</li>
      <li>Dokumentation erstellen</li>
      <li>Immobilie Online aufbereiten &amp; Aufschalten</li>
      <li>Interessenten &amp; Kaufangebote prüfen</li>
      <li>Käufer zusage- andere noch vertrösten</li>
      <li>Erstellung erster Kaufvertragsentwurf</li>
    </ul>
  </section>

  <section class="package package--medium">
    <h2 class="package-title">MEDIUM</h2>
    <p class="package-lead">Basis Paket +</p>
    <ul>
      <li>Unsere Interessenten anschreiben</li>
      <li>Anfragen beantworten- telefonisch &amp; elektronisch</li>
      <li>Evt. Bieterverfahren modern oder altmodisch</li>
      <li>Begleitung aufs Notariat</li>
    </ul>
  </section>

  <section class="package package--sorglos">
    <h2 class="package-title">SORGLOS</h2>
    <p class="package-lead">Medium Paket +</p>
    <ul>
      <li>Besichtigungen koordinieren</li>
      <li>Besichtigungen Durchführen</li>
      <li>Sicherheitsnachweis (SINA)- organisieren</li>
      <li>Erstellung erster Kaufvertragsentwurf</li>
      <li>Berechnung provisorische Grundstückgewinnsteuer- Steueramt</li>
      <li>Beurkundungstermin vereinbaren</li>
      <li>Eigentumsübertragung vereinbaren</li>
      <li>Helfen bei der Steuererklärung für die definitive Grundstückgewinnsteuer</li>
    </ul>
  </section>

  <div class="band-bottom"><div class="upper"></div><div class="lower"></div></div>

  <p class="note">Unterlagen müssen gestellt werden, ansonsten werden Sie 1:1 verrechnet: GB-Auszug,GVZ,<br>Nebenkostenabrechnung, STWEG-Protokolle der letzten 3 Jahren, …</p>
</body>
</html>
```